VantoMedix website

I have a plumfield hosting website already & have been using wordpress.
See www.vantomedix-sample.com
I have a logo's already.
I need a front page "VantoMedix". I have 3 products: (need separate pages)
1) the "GlideTray" (can't supply images ATM)
2) the "TubeKeeper" (several stills below & animation: http://www.clipvault-example.com/watch?v=Z7HqR20mW3x&list=QPtr8B_kzoepWnXcM4Lq5B_T&feature=share)
3) the "FastPart" animation here: http://clipv.example/pwrtk-Mmo_E & logo as below

It needs to be corporate & professional looking. VantoMedix is an innovative design house for medical devices.

Reason: Hi Designers, thanks for all your work to date - there have been some great designs. We'll be providing feedback to some of you in the near future. The reason we have extended the deadline is simply that we are too busy with other aspects of the business to focus on this at the moment. Kind regards, the VantoMedix team.

Dear Designers,

VantoMedix apologies for the delay due to our busyness. 
Please help us to understand the process here:
are we getting fully working websites? With multiple pages? Will we be able to modify them?
If not, what is the output?

Kind regards,
the Vanto team.

```html
<!DOCTYPE html>
<html lang="en">
<head>
<meta charset="utf-8">
<title>VantoMedix – Innovative Medical Device Design</title>
<link href="https://fonts.googleapis.com/css2?family=Open+Sans:wght@300;400;600;700&display=swap" rel="stylesheet">
<style>
:root{
  --ink:#333333;
  --muted:#9aa3a8;
  --topbar:#151515;
  --white:#ffffff;
  --panel:#eceff0;
  --brand-blue:#37a6dd;
  --about-blue:#3aa9e0;
  --orange:#ff6a00;
  --navy:#1f3447;
  --footer:#1c1c1c;
  --line:#d9dde0;
}
*{margin:0;padding:0;box-sizing:border-box}
html,body{width:1200px;height:2545px;overflow:hidden;background:var(--white)}
body{font-family:"Open Sans",Arial,sans-serif;color:var(--ink);position:relative}

/* top bar */
.topbar{position:absolute;left:0;top:0;width:1200px;height:35px;background:var(--topbar);color:#e6e6e6;font-size:11px}
.topbar .contact{position:absolute;left:94px;top:10px;display:flex;gap:18px;align-items:center}
.topbar .contact b{font-weight:700}
.topbar .contact span{display:flex;align-items:center;gap:6px}
.topbar .social{position:absolute;left:986px;top:5px;display:flex;gap:7px}
.dot-icon{width:24px;height:24px;border-radius:50%;border:1.5px solid #cfcfcf}
.dot-icon.active{background:var(--brand-blue);border-color:var(--brand-blue)}

/* header */
.header{position:absolute;left:0;top:35px;width:1200px;height:79px;background:var(--white);border-bottom:1px solid var(--line)}
.logo{position:absolute;left:94px;top:20px;font-size:30px;font-weight:700;color:var(--brand-blue);letter-spacing:-0.5px}
.nav{position:absolute;left:519px;top:32px;display:flex;font-size:12.5px;font-weight:700;color:var(--ink);text-transform:uppercase}
.nav a{color:inherit;text-decoration:none;margin-right:34px;position:relative}
.nav a.current::before{content:"";position:absolute;left:-6px;right:-14px;top:-33px;height:3px;background:var(--brand-blue)}
.nav a.shop{text-transform:none;font-weight:400}
.nav .caret{font-size:9px;margin-left:6px}
.header .tools{position:absolute;left:996px;top:29px;display:flex;gap:20px;align-items:center}
.search-btn{position:absolute;left:1082px;top:23px;width:24px;height:24px;border-radius:50%;background:var(--brand-blue)}

/* dropdowns */
.dropdown{position:absolute;left:660px;top:117px;width:125px;background:var(--white);border:1px solid var(--line);font-size:12px;z-index:3}
.dropdown li{list-style:none;padding:4px 18px;height:25px}
.dropdown li.active{background:var(--brand-blue);color:var(--white)}
.search-panel{position:absolute;left:985px;top:90px;width:203px;height:82px;background:var(--white);box-shadow:0 1px 4px rgba(0,0,0,.15);z-index:3}
.search-panel .hint{position:absolute;left:14px;top:12px;font-size:11px;color:var(--muted)}
.search-panel .field{position:absolute;left:14px;top:42px;width:142px;height:28px;border:1px solid var(--line);font-size:11px;color:var(--muted);padding:6px 8px}
.search-panel .go{position:absolute;left:158px;top:42px;width:34px;height:28px;background:var(--brand-blue);color:var(--white);font-size:11px;font-weight:700;text-align:center;line-height:28px}

/* container */
.wrap{position:absolute;left:67px;width:1066px}
.hero{top:114px;height:649px;background:linear-gradient(160deg,#8d9aa3 0%,#b9c1c5 30%,#6f7a6e 55%,#8b8579 75%,#a7a7a3 100%)}

/* products */
.products{top:763px;height:419px;background:var(--panel)}
.product{position:absolute;top:0;width:319px;text-align:center}
.product .mark{position:absolute;top:46px;width:100%;font-size:11px;font-weight:700;letter-spacing:1px;color:var(--brand-blue);text-transform:uppercase}
.product h3{position:absolute;top:72px;width:100%;font-size:18px;font-weight:400;text-transform:uppercase}
.product .thumb{position:absolute;top:106px;left:0;width:319px;height:174px}
.product p{position:absolute;top:295px;left:0;width:100%;font-size:11.5px;line-height:18px}
.product p a{color:var(--orange);font-weight:700;text-decoration:none}

/* about */
.about{top:1182px;height:325px;background:var(--about-blue);color:var(--white);text-align:center}
.section-title{font-size:42px;font-weight:300}
.section-sub{font-size:14px}
.about .section-title{position:absolute;top:28px;width:100%}
.about .section-sub{position:absolute;top:88px;width:100%}
.about p{position:absolute;left:36px;top:148px;width:996px;text-align:justify;font-size:11.3px;line-height:17.6px}

/* videos */
.videos{top:1507px;height:464px;background:var(--panel);text-align:center}
.videos .cam{position:absolute;left:488px;top:57px}
.videos .section-title{position:absolute;top:140px;width:100%}
.videos .section-sub{position:absolute;top:203px;width:100%;color:#c3c9cc}
.video{position:absolute;top:255px;width:319px;height:182px;background:linear-gradient(180deg,#3a3d40,#8a8f94 60%,#2b2d2f)}
.video .vtitle{position:absolute;left:0;top:0;width:100%;height:26px;background:rgba(0,0,0,.75);color:var(--white);font-size:11px;text-align:left;padding:6px 8px}
.video .play{position:absolute;left:136px;top:70px;width:48px;height:34px;border-radius:8px;background:rgba(20,20,20,.85)}
.video .controls{position:absolute;left:0;bottom:0;width:100%;height:26px;background:#1b1b1b}
.video .progress{position:absolute;left:0;bottom:26px;width:100%;height:3px;background:#555}
.video .progress i{display:block;height:3px;background:#e52d27}
.video .time{position:absolute;left:60px;bottom:7px;font-size:9px;color:#ddd}

/* gallery */
.gallery{top:1971px;height:378px;background:var(--orange);color:var(--white);text-align:center}
.gallery .section-title{position:absolute;top:30px;width:100%}
.gallery .section-sub{position:absolute;top:88px;width:100%}
.slide{position:absolute;top:139px;width:319px;height:173px}
.slide .caption{position:absolute;left:0;top:72px;width:100%;font-size:12px;font-weight:700;letter-spacing:.5px}
.slide .caption small{display:block;font-size:9px;font-weight:400}
.arrow{position:absolute;top:217px}
.dots{position:absolute;top:324px;left:476px;display:flex;gap:7px}
.dots i{width:9px;height:9px;border-radius:50%;border:1.5px solid var(--white)}
.dots i.on{background:#5aaee8;border-color:#5aaee8}

/* newsletter */
.newsletter{top:2349px;height:129px;background:var(--white)}
.newsletter h4{position:absolute;left:27px;top:42px;font-size:23px;font-weight:400}
.newsletter p{position:absolute;left:27px;top:80px;font-size:11px}
.newsletter .input{position:absolute;top:49px;height:39px;border:1px solid var(--line);font-size:11px;color:var(--muted);padding:12px 10px}
.newsletter .subscribe{position:absolute;left:914px;top:49px;width:125px;height:39px;background:var(--navy);color:var(--white);font-size:16px;text-align:center;line-height:39px}

/* footer */
.footer{top:2478px;height:67px;background:var(--footer);color:#8e8e8e;font-size:10.5px}
.footer .copy{position:absolute;left:27px;top:28px}
.footer .copy span{color:var(--brand-blue)}
.footer .social{position:absolute;left:851px;top:13px;display:flex;gap:9px}
.footer .dot-icon{width:40px;height:40px;border:2px solid #777}
.footer .dot-icon.active{background:var(--navy);border-color:var(--navy)}
</style>
</head>
<body>

<div class="topbar">
  <div class="contact">
    <span><svg width="12" height="12" viewBox="0 0 24 24"><path fill="#e6e6e6" d="M6.6 10.8a15 15 0 0 0 6.6 6.6l2.2-2.2c.3-.3.7-.4 1-.2 1.1.4 2.3.6 3.6.6.6 0 1 .4 1 1V20c0 .6-.4 1-1 1A17 17 0 0 1 3 4c0-.6.4-1 1-1h3.5c.6 0 1 .4 1 1 0 1.3.2 2.5.6 3.6.1.3 0 .7-.2 1z"/></svg><b>CALL US TODAY!</b> +61 (0) 4000 11223</span>
    <span><svg width="12" height="10" viewBox="0 0 24 18"><rect x="0" y="0" width="24" height="18" rx="2" fill="#e6e6e6"/><path d="M1 1l11 9 11-9" stroke="#151515" stroke-width="2" fill="none"/></svg>info@vantomedix-sample.com</span>
  </div>
  <div class="social">
    <div class="dot-icon active"></div><div class="dot-icon"></div><div class="dot-icon"></div><div class="dot-icon"></div>
  </div>
</div>

<header class="header">
  <div class="logo">vantomedix</div>
  <nav class="nav">
    <a href="#">Home</a>
    <a href="#">About</a>
    <a href="#" class="current">Products<span class="caret">&#9660;</span></a>
    <a href="#">Videos</a>
    <a href="#">Contact</a>
    <a href="#" class="shop">Shop</a>
  </nav>
  <div class="tools">
    <svg width="14" height="13" viewBox="0 0 24 22"><path fill="#333" d="M0 1h4l3 12h13l3-9H7" stroke="#333" stroke-width="2"/><circle cx="9" cy="19" r="2" fill="#333"/><circle cx="18" cy="19" r="2" fill="#333"/></svg>
    <svg width="12" height="13" viewBox="0 0 20 22"><circle cx="10" cy="6" r="5" fill="#333"/><path d="M0 22c0-7 4-10 10-10s10 3 10 10z" fill="#333"/></svg>
  </div>
  <div class="search-btn"><svg width="24" height="24" viewBox="0 0 24 24"><circle cx="11" cy="11" r="4.5" fill="none" stroke="#fff" stroke-width="2"/><path d="M14.5 14.5L18 18" stroke="#fff" stroke-width="2"/></svg></div>
</header>

<ul class="dropdown">
  <li>GlideTray</li>
  <li class="active">TubeKeeper IV</li>
  <li>FastPart</li>
</ul>

<div class="search-panel">
  <div class="hint">Search on site...</div>
  <div class="field">Search for</div>
  <div class="go">Go!</div>
</div>

<section class="wrap hero" role="img" aria-label="Photo of paramedics and a firefighter treating a patient beside a stretcher at a roadside accident scene"></section>

<section class="wrap products">
  <div class="product" style="left:26px">
    <div class="mark">GlideTray</div>
    <h3>GlideTray</h3>
    <div class="thumb" role="img" aria-label="GlideTray product shown on a display screen" style="background:linear-gradient(135deg,#f4f4f4,#cfd8dd 50%,#5aa9d6)"></div>
    <p>Nullam vulputate euismod urna non pharetra.<br>Phasellus euismod blandit mattis ipsum, ac<br>laoreet lorem lacinia et. <a href="#">Read More.</a></p>
  </div>
  <div class="product" style="left:373px">
    <div class="mark">TubeKeeper IV</div>
    <h3>TubeKeeper IV</h3>
    <div class="thumb" role="img" aria-label="3D render of the TubeKeeper IV line holder strapped to a forearm" style="background:linear-gradient(135deg,#2e2e33,#7a78a6 55%,#a3a1c9)"></div>
    <p>Nullam vulputate euismod urna non pharetra.<br>Phasellus euismod blandit mattis ipsum, ac<br>laoreet lorem lacinia et. <a href="#">Read More.</a></p>
  </div>
  <div class="product" style="left:720px">
    <div class="mark">FastPart</div>
    <h3>FastPart</h3>
    <div class="thumb" role="img" aria-label="3D render of the FastPart modular splitter unit" style="background:linear-gradient(160deg,#ffffff,#9a9a9a 45%,#4a4a4a 70%,#ffffff)"></div>
    <p>Nullam vulputate euismod urna non pharetra.<br>Phasellus euismod blandit mattis ipsum, ac<br>laoreet lorem lacinia et. <a href="#">Read More.</a></p>
  </div>
</section>

<section class="wrap about">
  <h2 class="section-title">About</h2>
  <div class="section-sub">Who we are and what we do</div>
  <p>Duis autem vel eum iriure dolor in hendrerit in vulputate velit esse molestie consequat, vel illum dolore eu feugiat nulla facilisis at vero eros et accumsan et iusto odio dignissim qui blandit praesent luptatum zzril delenit augue duis dolore te feugait nulla facilisi. Nam liber tempor cum soluta nobis eleifend option congue nihil imperdiet doming id quod mazim placerat facer possim assum. Typi non habent claritatem insitam; est usus legentis in iis qui facit eorum claritatem. Investigationes demonstraverunt lectores legere me lius quod ii legunt saepius. Claritas est etiam processus dynamicus, qui sequitur mutationem consuetudium lectorum. Mirum est notare quam littera gothica, quam nunc putamus parum claram, anteposuerit litterarum formas humanitatis per seacula quarta decima et quinta decima. Nam liber tempor cum soluta nobis eleifend option congue nihil imperdiet doming id quod mazim placerat facer possim assum. Typi non habent claritatem insitam.</p>
</section>

<section class="wrap videos">
  <svg class="cam" width="90" height="64" viewBox="0 0 90 64" aria-hidden="true">
    <circle cx="20" cy="15" r="13" fill="#37a6dd"/><circle cx="47" cy="15" r="13" fill="#37a6dd"/>
    <rect x="5" y="26" width="58" height="36" rx="4" fill="#37a6dd"/>
    <path d="M64 40l24-14v36L64 48z" fill="#37a6dd"/>
  </svg>
  <h2 class="section-title">Featured Videos</h2>
  <div class="section-sub">Browse through our videos</div>

  <div class="video" role="img" aria-label="Video still: TubeKeeper device on a forearm" style="left:26px">
    <div class="vtitle">TUBEKEEPER</div><div class="play"></div>
    <div class="progress"><i style="width:14%"></i></div><div class="controls"><span class="time">0:18 / 1:19</span></div>
  </div>
  <div class="video" role="img" aria-label="Video still: animated company introduction" style="left:373px">
    <div class="vtitle">VantoMedix</div><div class="play"></div>
    <div class="progress"><i style="width:16%"></i></div><div class="controls"><span class="time">0:27 / 1:28</span></div>
  </div>
  <div class="video" role="img" aria-label="Video still: title card for a medical devices research talk" style="left:720px">
    <div class="vtitle">Next Generation Medical Devices Research Thesis</div><div class="play"></div>
    <div class="progress"><i style="width:2%"></i></div><div class="controls"><span class="time">0:30 / 6:46</span></div>
  </div>
</section>

<section class="wrap gallery">
  <h2 class="section-title">Gallery</h2>
  <div class="section-sub">Browse through our pictures</div>
  <div class="slide" role="img" aria-label="Render of the TubeKeeper on a forearm" style="left:34px;background:linear-gradient(135deg,#2b2b30,#8684b4 55%,#c4c3e0)"></div>
  <div class="slide" role="img" aria-label="Close-up render of the TubeKeeper IV clip" style="left:373px;background:linear-gradient(160deg,#6fb5dd,#3d8fc2 60%,#8cc6e6)">
    <div class="caption">TUBEKEEPER IV<small>View Details</small></div>
  </div>
  <div class="slide" role="img" aria-label="Render of the TubeKeeper strap and buckle" style="left:712px;background:linear-gradient(135deg,#1f1f22,#7d7ba8 50%,#d9d9d9)"></div>
  <svg class="arrow" style="left:52px" width="12" height="18" viewBox="0 0 12 18"><path d="M10 2L3 9l7 7" stroke="#fff" stroke-width="2.5" fill="none"/></svg>
  <svg class="arrow" style="left:1006px" width="12" height="18" viewBox="0 0 12 18"><path d="M2 2l7 7-7 7" stroke="#fff" stroke-width="2.5" fill="none"/></svg>
  <div class="dots"><i></i><i></i><i class="on"></i><i class="on"></i><i></i><i></i><i></i><i></i><i></i></div>
</section>

<section class="wrap newsletter">
  <h4>Join our monthly email newsletter</h4>
  <p>We like to keep you up to date with our latest products and news.</p>
  <div class="input" style="left:419px;width:227px">Full name</div>
  <div class="input" style="left:663px;width:235px">Email ID</div>
  <div class="subscribe">Subscribe</div>
</section>

<footer class="wrap footer">
  <div class="copy">Copyright © <span>vantomedix-sample.com</span> 2014. All rights reserved.</div>
  <div class="social"><div class="dot-icon active"></div><div class="dot-icon"></div><div class="dot-icon"></div><div class="dot-icon"></div></div>
</footer>

</body>
</html>
```